Hadley & Partners, LLC Business Card 2016

We need a new business card design for a very important trade show coming up.

We are a compliance Consulting Firm. Our clients are stock brokerage firms and investment advisers.

I would like our logo on both sides of the card.

Info in the front of the card shold include:

Logo
First & Last Name
Title
Office #
Cell #
Email
Company Address (42 W. Calloway St., Suite 300 Pasadena, CA 91417

Back of the card should include the logo and url: www.hadleypartnersgroup.com

Target Market(s)

Stock Brokerage Firms and Investment Advisers

Industry/Entity Type

Financial Service

Contact Information for Business Card

Marcus J. Pellew
President
42 W. Calloway St., Suite 300
Pasadena, CA 91417
O 626.555.0147 ext. 204
C 818.555.0193
Email: marcus@hadleypartnersgroup.com
www.hadleypartnersgroup.com

Requirements
Nice to have
• The back of the card could be black with the logo with the white letters.
• I do want the front of the card to at least have the color logo with the black "Hadley & Partners Lettering.

```html
<!DOCTYPE html>
<html lang="en">
<head>
<meta charset="utf-8">
<title>Hadley &amp; Partners — Business Card</title>
<link href="https://fonts.googleapis.com/css2?family=PT+Sans:wght@400;700&display=swap" rel="stylesheet">
<style>
  :root {
    --backdrop: #4a3139;
    --card: #231f20;
    --white: #ffffff;
    --red: #e3262b;
    --red-dark: #b51d22;
    --grey-light: #8a8c90;
    --grey-dark: #4a4c50;
  }
  * { margin: 0; padding: 0; box-sizing: border-box; }
  html, body {
    width: 1200px; height: 1200px; overflow: hidden;
    background: var(--backdrop);
    font-family: "PT Sans", sans-serif;
    color: var(--white);
  }
  .card {
    position: absolute; left: 208px; width: 785px; height: 448px;
    background: var(--card); border-radius: 20px; overflow: hidden;
  }
  .card--back { top: 120px; }
  .card--front { top: 635px; }

  .brand { position: absolute; display: flex; align-items: center; }
  .brand__mark { background: var(--red); }
  .brand__name {
    font-weight: 700; color: var(--white); text-transform: uppercase;
    white-space: nowrap;
  }
  .card--back .brand { left: 0; right: 0; top: 176px; justify-content: center; gap: 22px; }
  .card--back .brand__mark { width: 62px; height: 62px; }
  .card--back .brand__name { font-size: 52px; letter-spacing: 1px; }
  .card--back .site {
    position: absolute; left: 0; right: 0; top: 362px;
    text-align: center; font-size: 20px;
  }

  .card--front .brand { right: 45px; top: 52px; gap: 14px; }
  .card--front .brand__mark { width: 38px; height: 38px; }
  .card--front .brand__name { font-size: 32px; letter-spacing: 0.5px; }

  .accent-bar {
    position: absolute; left: 0; top: 151px; width: 16px; height: 55px;
    background: linear-gradient(90deg, var(--red-dark), var(--red));
  }
  .person { position: absolute; left: 44px; top: 148px; }
  .person__name { font-size: 30px; line-height: 36px; }
  .person__title { font-size: 21px; line-height: 24px; color: var(--red); }
  .address { position: absolute; left: 44px; top: 233px; font-size: 20px; line-height: 26px; }
  .contacts { position: absolute; left: 44px; top: 297px; list-style: none; font-size: 20px; }
  .contacts li { display: flex; align-items: center; height: 26px; }
  .contacts svg { width: 18px; height: 18px; margin-right: 14px; fill: var(--red); }

  .stripe { position: absolute; left: 0; bottom: 0; width: 100%; height: 16px; }
</style>
</head>
<body>
  <section class="card card--back">
    <div class="brand">
      <span class="brand__mark"></span>
      <span class="brand__name">Hadley &amp; Partners</span>
    </div>
    <p class="site">www.hadleypartnersgroup.com</p>
  </section>

  <section class="card card--front">
    <div class="brand">
      <span class="brand__mark"></span>
      <span class="brand__name">Hadley &amp; Partners</span>
    </div>

    <span class="accent-bar"></span>
    <div class="person">
      <h1 class="person__name">Marcus J. Pellew</h1>
      <p class="person__title">President</p>
    </div>
    <p class="address">42 W. Calloway St., Suite 300<br>Pasadena, CA 91417</p>

    <ul class="contacts">
      <li>
        <svg viewBox="0 0 20 20"><path d="M1 7c0-3 4-5 9-5s9 2 9 5v2h-5V7H6v2H1z"/><path d="M5 10h10l3 8H2z"/><circle cx="10" cy="14" r="2.2" fill="#231f20"/></svg>
        626.555.0147 ext. 204
      </li>
      <li>
        <svg viewBox="0 0 20 20"><path d="M5 1h10a1 1 0 0 1 1 1v16a1 1 0 0 1-1 1H5a1 1 0 0 1-1-1V2a1 1 0 0 1 1-1zm1 2v12h8V3z"/><circle cx="10" cy="17" r="1" fill="#231f20"/></svg>
        818.555.0193
      </li>
      <li>
        <svg viewBox="0 0 20 20"><path d="M1 4h18v12H1z"/><path d="M1 4l9 7 9-7M1 16l7-6M19 16l-7-6" stroke="#231f20" stroke-width="1.3" fill="none"/></svg>
        marcus@hadleypartnersgroup.com
      </li>
      <li>
        <svg viewBox="0 0 20 20"><g fill="none" stroke="#e3262b" stroke-width="1.4"><circle cx="10" cy="10" r="8.2"/><ellipse cx="10" cy="10" rx="3.6" ry="8.2"/><path d="M2 10h16M3.5 5.5h13M3.5 14.5h13"/></g></svg>
        www.hadleypartnersgroup.com
      </li>
    </ul>

    <svg class="stripe" viewBox="0 0 785 16" preserveAspectRatio="none">
      <defs>
        <linearGradient id="stripe-grey" x1="0" x2="1">
          <stop offset="0" stop-color="#4a4c50"/><stop offset="1" stop-color="#8a8c90"/>
        </linearGradient>
        <linearGradient id="stripe-red" x1="0" x2="1">
          <stop offset="0" stop-color="#e3262b"/><stop offset="1" stop-color="#b51d22"/>
        </linearGradient>
      </defs>
      <polygon points="0,0 420,0 404,16 0,16" fill="url(#stripe-grey)"/>
      <polygon points="425,0 785,0 785,16 409,16" fill="url(#stripe-red)"/>
    </svg>
  </section>
</body>
</html>
```